Granite Surface Works, Inc. Business Card

New business, we do epoxy, polishing concrete, underlayment, fluid applied flooring, sound proofing, double sided, will need 3 sets of cards with 3 different names and phone numbers.
Company: Granite Surface Works, Inc.
Address and Phone: 6339 Charlotte Pike PMB 2183Nashville, TN 37209
(615) 384-7190
www.granitesurfaceworks.example

Target Market(s)

General Contractors, Contractors, Architects

Contact Information for Business Card

1st Card: Derek Halvorsen C. 708.214.8573 e. derek@granitesurfaceworks.example
Vice President
2nd Card: Morgan Brasfield C. 708.361.5847 e. morgan@granitesurfaceworks.example
President
3rd Card: Raj Oti C. 405.617.3328 e. raj@granitesurfaceworks.example
Managing Partner

Font styles to use
Serif
Sans Serif

Requirements
Must have
• Professional Clean Design, Implement colors from Logo or nicely contrasting
Nice to have
• N/A

```html
<!DOCTYPE html>
<html lang="en">
<head>
<meta charset="utf-8">
<title>Granite Surface Works, Inc. Business Card</title>
<link rel="stylesheet" href="https://fonts.googleapis.com/css2?family=Roboto:wght@400;500;700&display=swap">
<style>
  :root {
    --brand-blue: #0a62b0;
    --brand-green: #6aa83c;
    --ink: #1c1c1c;
    --card-white: #f6f7f9;
    --backdrop: #e4e6ea;
  }
  * { margin: 0; padding: 0; box-sizing: border-box; }
  html, body {
    width: 1200px; height: 960px; overflow: hidden;
    background: var(--backdrop);
    font-family: "Roboto", Arial, sans-serif;
  }
  .sheet {
    width: 1200px; height: 960px;
    display: flex; flex-direction: column;
    align-items: center; justify-content: center; gap: 54px;
  }
  .card {
    width: 700px; height: 400px;
    box-shadow: 0 6px 18px rgba(0,0,0,.18);
    position: relative;
  }
  .card-front {
    background: var(--brand-blue);
    display: flex; align-items: center; justify-content: center;
  }
  .wordmark {
    display: flex; align-items: center; gap: 14px;
    font-weight: 700; font-size: 34px; letter-spacing: .5px;
  }
  .wordmark-square { width: 28px; height: 28px; flex: none; }
  .card-front .wordmark { color: #ffffff; }
  .card-front .wordmark-square { background: #ffffff; }

  .card-back { background: var(--card-white); }
  .card-back .wordmark {
    position: absolute; left: 60px; top: 178px;
    font-size: 22px; gap: 10px; color: var(--ink);
  }
  .card-back .wordmark-square { width: 20px; height: 20px; background: var(--brand-blue); }

  .contact-block {
    position: absolute; left: 368px; top: 64px;
    color: var(--ink); font-size: 16px; line-height: 1.3;
  }
  .person-name { color: var(--brand-blue); font-weight: 700; font-size: 24px; }
  .person-title { color: var(--brand-green); font-size: 16px; margin-bottom: 22px; }
  .company-name { color: var(--brand-blue); font-weight: 500; font-size: 16px; }
  .address { margin-bottom: 18px; }
  .contact-list { list-style: none; }
  .contact-list li { display: flex; align-items: center; gap: 12px; line-height: 26px; }
  .contact-icon { width: 14px; height: 14px; flex: none; fill: var(--brand-blue); }
</style>
</head>
<body>
<main class="sheet">
  <section class="card card-front" aria-label="Card front">
    <div class="wordmark"><span class="wordmark-square"></span>Granite Surface Works</div>
  </section>

  <section class="card card-back" aria-label="Card back">
    <div class="wordmark"><span class="wordmark-square"></span>Granite Surface Works</div>

    <div class="contact-block">
      <p class="person-name">Derek Halvorsen</p>
      <p class="person-title">Vice President</p>
      <p class="company-name">Granite Surface Works, Inc.</p>
      <p class="address">4817 Willowmere Road PMB 5046<br>Nashville, TN 37209</p>
      <ul class="contact-list">
        <li>
          <svg class="contact-icon" viewBox="0 0 16 16" aria-hidden="true"><path d="M3 1l3 3-1.6 2a9 9 0 0 0 5.6 5.6L12 10l3 3-2 2C7 15 1 9 1 3z"/></svg>
          (615) 384-7190
        </li>
        <li>
          <svg class="contact-icon" viewBox="0 0 16 16" aria-hidden="true"><path d="M4 0h8a1 1 0 0 1 1 1v14a1 1 0 0 1-1 1H4a1 1 0 0 1-1-1V1a1 1 0 0 1 1-1zm1 2v10h6V2zm3 11a1 1 0 1 0 0 2 1 1 0 0 0 0-2z"/></svg>
          708.214.8573
        </li>
        <li>
          <svg class="contact-icon" viewBox="0 0 16 16" aria-hidden="true"><path d="M1 3h14v10H1zm1 1.2V5l6 4 6-4v-.8L8 8z"/></svg>
          derek@granitesurfaceworks.example
        </li>
        <li>
          <svg class="contact-icon" viewBox="0 0 16 16" aria-hidden="true"><circle cx="8" cy="8" r="7"/></svg>
          www.granitesurfaceworks.example
        </li>
      </ul>
    </div>
  </section>
</main>
</body>
</html>
```